Bright Sprouts Business Card

speech therapy business card that is fun and professional using my logo.
Updates

Wow wonderful dedigns ... 

Industry/Entity Type

Business

Contact Information for Business Card

Tessa Morvan
Brelow Certified Practising Speech Pathologist
B.Sp.Path MSPAA CPSP
ph: 0413906281
brightsproutsspeechpathology@mailbox.example
www.brightsproutsspeechpathology.example

```html
<!DOCTYPE html>
<html lang="en">
<head>
<meta charset="utf-8">
<title>Bright Sprouts Speech Pathology – Business Cards</title>
<link rel="stylesheet" href="https://fonts.googleapis.com/css2?family=Open+Sans:wght@400;600&family=Michroma&display=swap">
<style>
  :root {
    --backdrop: #2b2b2b;
    --card-sky: #6cbbe8;
    --card-sky-light: #8fcdf0;
    --band: #4a9fd3;
    --ink-blue: #2f7fb8;
    --ink-navy: #1f3b66;
    --white: #ffffff;
    --plum: #5e2a78;
  }
  * { box-sizing: border-box; margin: 0; padding: 0; }
  html, body { width: 960px; height: 1200px; overflow: hidden; }
  body {
    background: var(--backdrop);
    font-family: "Open Sans", Arial, sans-serif;
    position: relative;
  }
  .card {
    position: absolute;
    left: 219px;
    width: 543px;
    height: 301px;
    overflow: hidden;
    background:
      radial-gradient(circle at 28% 60%, rgba(255,255,255,0.55) 0, rgba(255,255,255,0.12) 60px, rgba(255,255,255,0) 150px),
      linear-gradient(180deg, var(--card-sky-light), var(--card-sky) 40%);
  }
  .card--front { top: 79px; }
  .card--back-a { top: 455px; }
  .card--back-b { top: 823px; }

  .glow {
    position: absolute;
    left: 0; top: 0;
    width: 260px; height: 301px;
    background: radial-gradient(ellipse at 40% 70%, rgba(255,255,255,0.35), rgba(255,255,255,0) 70%);
  }

  .brand-dot {
    position: absolute;
    border-radius: 50%;
    background: var(--plum);
  }
  .brand-name {
    position: absolute;
    color: var(--ink-blue);
    font-weight: 400;
    line-height: 1.15;
    white-space: nowrap;
  }
  .card--front .brand-dot { left: 86px; top: 124px; width: 76px; height: 76px; }
  .card--front .brand-name { left: 185px; top: 134px; font-size: 27px; }

  .card--back-a .brand-dot,
  .card--back-b .brand-dot { left: 105px; top: 50px; width: 44px; height: 44px; }
  .card--back-a .brand-name,
  .card--back-b .brand-name { left: 30px; top: 125px; font-size: 26px; }

  .web-band {
    position: absolute;
    right: 0; bottom: 0;
    width: 290px; height: 24px;
    background: var(--band);
    clip-path: polygon(10px 0, 100% 0, 100% 100%, 0 100%);
    color: var(--white);
    font-size: 12px;
    line-height: 24px;
    padding-left: 20px;
    white-space: nowrap;
  }

  .person-name {
    position: absolute;
    left: 302px; top: 127px;
    color: var(--white);
    font-size: 25px;
    font-weight: 400;
    white-space: nowrap;
  }
  .person-title {
    position: absolute;
    left: 302px; top: 158px;
    width: 241px; height: 13px;
    background: var(--white);
    color: var(--ink-blue);
    font-family: "Michroma", Arial, sans-serif;
    font-size: 5.3px;
    letter-spacing: 0.25px;
    line-height: 13px;
    padding-left: 5px;
    white-space: nowrap;
  }
  .person-credentials {
    position: absolute;
    right: 7px; top: 177px;
    color: var(--white);
    font-size: 11px;
    white-space: nowrap;
  }
  .contact-band {
    position: absolute;
    left: 268px; top: 210px;
    width: 275px; height: 54px;
    background: var(--band);
    clip-path: polygon(15px 0, 100% 0, 100% 100%, 0 100%);
    padding: 6px 0 0 20px;
    color: var(--white);
    font-size: 9.2px;
    list-style: none;
  }
  .contact-band li { display: flex; align-items: center; height: 15.5px; white-space: nowrap; }
  .contact-band svg { width: 14px; height: 12px; margin-right: 6px; flex: none; }

  .social {
    position: absolute;
    left: 9px; top: 280px;
    display: flex; align-items: center;
    color: var(--ink-navy);
    font-size: 9.6px;
    font-weight: 600;
    white-space: nowrap;
  }
  .social-name {
    color: var(--ink-navy);
    font-weight: 600;
    margin-right: 8px;
  }
</style>
</head>
<body>

<section class="card card--front" aria-label="Business card front">
  <div class="glow" role="img" aria-label="Soft light bubbles"></div>
  <div class="brand-dot"></div>
  <p class="brand-name">Bright Sprouts<br>Speech Pathology</p>
  <p class="web-band">www.brightsproutsspeechpathology.example</p>
</section>

<section class="card card--back-a" aria-label="Business card back">
  <div class="glow" role="img" aria-label="Soft light bubbles"></div>
  <div class="brand-dot"></div>
  <p class="brand-name">Bright Sprouts<br>Speech Pathology</p>
  <h2 class="person-name">Tessa Morvan</h2>
  <p class="person-title">BRELOW CERTIFIED PRACTISING SPEECH PATHOLOGIST</p>
  <p class="person-credentials">B.Sp.Path MSPAA CPSP</p>
  <ul class="contact-band">
    <li><svg viewBox="0 0 14 12"><path fill="#fff" d="M1 4c0-2 2-3 6-3s6 1 6 3v1h-3V3.8H4V5H1zM3 6h8l1.5 5h-11z"/></svg>ph: 0413906281</li>
    <li><svg viewBox="0 0 14 12"><rect x="1" y="2" width="12" height="8" fill="none" stroke="#fff" stroke-width="1.3"/><path d="M1 2l6 5 6-5" fill="none" stroke="#fff" stroke-width="1.3"/></svg>brightsproutsspeechpathology@mailbox.example</li>
    <li><svg viewBox="0 0 14 12"><circle cx="7" cy="6" r="5.2" fill="none" stroke="#fff" stroke-width="1.1"/><ellipse cx="7" cy="6" rx="2.3" ry="5.2" fill="none" stroke="#fff" stroke-width="1"/><path d="M2 6h10M2.8 3.5h8.4M2.8 8.5h8.4" stroke="#fff" stroke-width="0.9"/></svg>www.brightsproutsspeechpathology.example</li>
  </ul>
  <p class="social"><span class="social-name">Chatterly</span>chatterly.example/BrightSproutsSpeechPathology</p>
</section>

<section class="card card--back-b" aria-label="Business card back, alternate">
  <div class="glow" role="img" aria-label="Soft light bubbles"></div>
  <div class="brand-dot"></div>
  <p class="brand-name">Bright Sprouts<br>Speech Pathology</p>
  <h2 class="person-name">Tessa Morvan</h2>
  <p class="person-title">BRELOW CERTIFIED PRACTISING SPEECH PATHOLOGIST</p>
  <p class="person-credentials">B.Sp.Path MSPAA CPSP</p>
  <ul class="contact-band">
    <li><svg viewBox="0 0 14 12"><path fill="#fff" d="M1 4c0-2 2-3 6-3s6 1 6 3v1h-3V3.8H4V5H1zM3 6h8l1.5 5h-11z"/></svg>ph: 0413906281</li>
    <li><svg viewBox="0 0 14 12"><rect x="1" y="2" width="12" height="8" fill="none" stroke="#fff" stroke-width="1.3"/><path d="M1 2l6 5 6-5" fill="none" stroke="#fff" stroke-width="1.3"/></svg>brightsproutsspeechpathology@mailbox.example</li>
    <li><svg viewBox="0 0 14 12"><circle cx="7" cy="6" r="5.2" fill="none" stroke="#fff" stroke-width="1.1"/><ellipse cx="7" cy="6" rx="2.3" ry="5.2" fill="none" stroke="#fff" stroke-width="1"/><path d="M2 6h10M2.8 3.5h8.4M2.8 8.5h8.4" stroke="#fff" stroke-width="0.9"/></svg>www.brightsproutsspeechpathology.example</li>
  </ul>
  <p class="social"><span class="social-name">Chatterly</span>chatterly.example/BrightSproutsSpeechPathology</p>
</section>

</body>
</html>
```